Welding company needs a business card

We are looking for a logo and business card.

Contact Information for Business Card

418 Cobblestone Lane
York, PA 17402
410-555-0173
Rmfabworksco@quorvamail.com

```html
<!DOCTYPE html>
<html lang="en">
<head>
<meta charset="utf-8">
<title>RM Fabworks Co. — Business Cards</title>
<link rel="stylesheet" href="https://fonts.googleapis.com/css2?family=Michroma&family=Lato:wght@400&display=swap">
<style>
  :root {
    --stage: #1a1a1a;
    --card: #262424;
    --red: #d0232a;
    --white: #ffffff;
    --soft: #e9e9e9;
  }
  * { margin: 0; padding: 0; box-sizing: border-box; }
  html, body { width: 1200px; height: 895px; overflow: hidden; background: var(--stage); }
  .canvas { position: relative; width: 1200px; height: 895px; }
  .card {
    position: absolute; left: 290px; width: 620px; height: 354px;
    background: var(--card); box-shadow: 0 10px 30px rgba(0,0,0,.55);
  }
  .card--front { top: 70px; }
  .card--back { top: 471px; }
  .brand-name {
    position: absolute; left: 42px; top: 70px;
    font-family: "Michroma", sans-serif; font-size: 25px; letter-spacing: 1px;
    color: var(--white); text-transform: uppercase; white-space: nowrap;
  }
  .brand-mark {
    position: absolute; left: 452px; top: 42px; width: 120px; height: 120px;
    border-radius: 50%; border: 12px solid var(--red);
  }
  .person { position: absolute; left: 42px; }
  .card--front .person { top: 150px; }
  .card--back .person { top: 170px; }
  .person-name {
    font-family: "Michroma", sans-serif; font-size: 20px; color: var(--red);
    text-transform: uppercase; letter-spacing: .5px;
  }
  .person-title {
    font-family: "Lato", sans-serif; font-size: 14px; color: var(--soft); margin-top: 4px; letter-spacing: .5px;
  }
  .contacts { position: absolute; left: 42px; list-style: none; }
  .card--front .contacts { top: 222px; }
  .card--back .contacts { top: 262px; }
  .contact {
    display: flex; align-items: center; gap: 12px; height: 28px;
    font-family: "Lato", sans-serif; font-size: 15px; color: var(--soft); letter-spacing: .5px;
  }
  .contact svg { width: 14px; height: 14px; flex: none; }
  .address-aside {
    position: absolute; right: 44px; top: 186px; text-align: right;
    font-family: "Lato", sans-serif; font-size: 15px; color: var(--soft); letter-spacing: .5px;
  }
</style>
</head>
<body>
<main class="canvas">

  <article class="card card--front">
    <h1 class="brand-name">RM Fabworks Co.</h1>
    <div class="brand-mark" aria-hidden="true"></div>
    <div class="person">
      <p class="person-name">Dale Rourke</p>
      <p class="person-title">Operations Manager</p>
    </div>
    <ul class="contacts">
      <li class="contact">
        <svg viewBox="0 0 14 14" aria-hidden="true"><rect x="3" y="1" width="8" height="12" rx="1.5" fill="none" stroke="#d0232a" stroke-width="1.5"/><line x1="6" y1="11" x2="8" y2="11" stroke="#d0232a" stroke-width="1.2"/></svg>
        410-555-0173
      </li>
      <li class="contact">
        <svg viewBox="0 0 14 14" aria-hidden="true"><rect x="1" y="3" width="12" height="8" fill="none" stroke="#d0232a" stroke-width="1.4"/><polyline points="1,3 7,8 13,3" fill="none" stroke="#d0232a" stroke-width="1.4"/></svg>
        Rmfabworksco@quorvamail.com
      </li>
      <li class="contact">
        <svg viewBox="0 0 14 14" aria-hidden="true"><path d="M7 13 C3 8 2.5 6.5 2.5 5 A4.5 4.5 0 0 1 11.5 5 C11.5 6.5 11 8 7 13 Z" fill="#d0232a"/><circle cx="7" cy="5" r="1.6" fill="#262424"/></svg>
        418 Cobblestone Lane, York, PA 17402
      </li>
    </ul>
  </article>

  <article class="card card--back">
    <h2 class="brand-name">RM Fabworks Co.</h2>
    <div class="brand-mark" aria-hidden="true"></div>
    <p class="address-aside">418 Cobblestone Lane, York, PA 17402</p>
    <div class="person">
      <p class="person-name">Evan Marsh</p>
      <p class="person-title">Operations Manager</p>
    </div>
    <ul class="contacts">
      <li class="contact">
        <svg viewBox="0 0 14 14" aria-hidden="true"><rect x="3" y="1" width="8" height="12" rx="1.5" fill="none" stroke="#d0232a" stroke-width="1.5"/><line x1="6" y1="11" x2="8" y2="11" stroke="#d0232a" stroke-width="1.2"/></svg>
        410-555-0173
      </li>
      <li class="contact">
        <svg viewBox="0 0 14 14" aria-hidden="true"><rect x="1" y="3" width="12" height="8" fill="none" stroke="#d0232a" stroke-width="1.4"/><polyline points="1,3 7,8 13,3" fill="none" stroke="#d0232a" stroke-width="1.4"/></svg>
        Rmfabworksco@quorvamail.com
      </li>
    </ul>
  </article>

</main>
</body>
</html>
```